Simple+Professional tech feel + warm and friendly box design for pet test kit

Project Name: 10-Minute Canine & Feline Rapid Test Kit Packaging Design
Target Brand Reference: VELUMAR (South Korea) styles
Design Style Direction: Professional tech feel + warm and friendly
Professionalism (Professional): Clear typography and distinct information hierarchy to reflect the product’s scientific rigor and accuracy.
Technological: Reflected through clean graphics and a minimalist layout.
Friendly: Utilise soft, warm colour combinations to convey care for pets and well-wishes for their health.
International: The design should align with mainstream aesthetics and avoid cultural ambiguities.

Target Market(s)
European Union and the United States
Industry/Entity Type
Veterinary Medical
Look and feel
Each slider illustrates characteristics of the customer's brand and the style your logo design should communicate.

```html
<!DOCTYPE html>
<html lang="en">
<head>
<meta charset="utf-8">
<title>PetLumo Rapid Test Kit – Carton Dieline</title>
<link href="https://fonts.googleapis.com/css2?family=Montserrat:wght@400;500;600;700&family=Source+Sans+3:wght@400;600&display=swap" rel="stylesheet">
<style>
  :root{
    --paper:#ffffff;
    --panel:#f3f2f0;
    --teal:#9dd1c9;
    --ink:#111111;
    --cut:#4a4a4a;
    --bleed:#f2a3a8;
    --fold:#8a8a8a;
    --art:#d9dcd9;
  }
  html,body{margin:0;padding:0;width:1200px;height:1200px;overflow:hidden;background:var(--paper);}
  .dieline{display:block;width:1200px;height:1200px;}
  .size-label{font-family:"Source Sans 3",sans-serif;font-size:44px;fill:var(--ink);}
  .brand{font-family:"Montserrat",sans-serif;font-weight:600;fill:var(--ink);}
  .tm{font-family:"Montserrat",sans-serif;font-weight:500;fill:var(--ink);}
  .maker{font-family:"Montserrat",sans-serif;font-weight:500;fill:var(--ink);}
  .copy{font-family:"Montserrat",sans-serif;fill:var(--ink);}
  .copy-bold{font-family:"Montserrat",sans-serif;font-weight:700;fill:var(--ink);}
  .badge-text{font-family:"Source Sans 3",sans-serif;font-weight:600;fill:var(--ink);}
  .contact{font-family:"Source Sans 3",sans-serif;font-size:12px;fill:var(--ink);}
  .note{font-family:"Source Sans 3",sans-serif;font-weight:600;font-size:12.5px;fill:var(--ink);}
  .story{font-family:"Montserrat",sans-serif;font-size:15px;fill:var(--ink);}
  .cut{fill:none;stroke:var(--cut);stroke-width:1.2;}
  .bleed{fill:none;stroke:var(--bleed);stroke-width:1.2;}
  .fold{fill:none;stroke:var(--fold);stroke-width:1;stroke-dasharray:5 4;}
  .icon{fill:none;stroke:var(--ink);stroke-width:1.6;stroke-linecap:round;stroke-linejoin:round;}
  .panel-bg{fill:var(--panel);}
  .teal-band{fill:var(--teal);}
  .art-placeholder{fill:var(--art);}
</style>
</head>
<body>
<svg class="dieline" viewBox="0 0 1920 1920" xmlns="http://www.w3.org/2000/svg">
  <text class="size-label" x="965" y="333" text-anchor="middle">Size: 135*65*90mm</text>

  <!-- printed panels -->
  <g class="print-areas">
    <path class="panel-bg" d="M202 845 V570 Q202 541 231 541 H705 Q733 541 733 570 V845 Z"/>
    <rect class="panel-bg" x="202" y="845" width="531" height="262"/>
    <rect class="teal-band" x="202" y="1107" width="531" height="91"/>
    <rect class="teal-band" x="733" y="845" width="257" height="142"/>
    <rect class="panel-bg" x="733" y="987" width="257" height="53"/>
    <rect class="teal-band" x="733" y="1040" width="257" height="87"/>
    <rect class="panel-bg" x="990" y="845" width="531" height="262"/>
    <rect class="teal-band" x="990" y="1107" width="531" height="91"/>
    <rect class="panel-bg" x="1521" y="845" width="256" height="353"/>
  </g>

  <!-- bleed outline -->
  <path class="bleed" d="M190 835 V560 Q190 529 221 529 H715 Q745 529 745 560 V706 H940 Q958 706 964 724 L987 812 L1002 824 V832 H1509 V824 L1524 812 L1547 724 Q1553 706 1571 706 H1775 V830 L1789 843 V1203 L1662 1340 V1365 Q1662 1387 1640 1387 H1509 V1228 L1400 1332 V1380 Q1400 1402 1378 1402 H1133 Q1110 1402 1110 1380 V1332 L1002 1228 V1387 H871 Q849 1387 849 1365 V1335 L745 1228 V1402 H611 Q589 1402 589 1380 V1338 H347 V1380 Q347 1402 325 1402 H190 V1207 L143 1193 V849 Z"/>

  <!-- cut lines -->
  <g class="cut">
    <path d="M202 845 V570 Q202 541 231 541 H705 Q733 541 733 570 V845"/>
    <path d="M202 858 L155 872 V1183 L202 1196"/>
    <path d="M202 1198 V1390 H315 Q335 1390 335 1370 V1327 H601 V1370 Q601 1390 621 1390 H733 V1198"/>
    <path d="M733 1198 L861 1327 V1360 Q861 1375 876 1375 H990 V1198"/>
    <path d="M990 1198 L1122 1327 V1375 Q1122 1390 1138 1390 H1373 Q1388 1390 1388 1375 V1327 L1521 1198"/>
    <path d="M1521 1198 V1375 H1635 Q1650 1375 1650 1360 V1333 L1777 1198"/>
    <path d="M733 845 V835 L747 822 V718 H940 Q950 718 954 728 L977 818 L990 830 V845"/>
    <path d="M1521 845 V830 L1535 818 L1560 727 Q1565 718 1575 718 H1763 V830 L1777 845 V1198"/>
    <path d="M990 845 H1521"/>
    <path d="M202 845 V1198"/>
    <path d="M245 588 V609 M691 588 V609"/>
  </g>

  <!-- fold lines -->
  <g class="fold">
    <path d="M202 588 H733"/>
    <path d="M202 845 H1777"/>
    <path d="M202 1198 H1777"/>
    <path d="M733 845 V1198 M990 845 V1198 M1521 845 V1198"/>
  </g>

  <!-- top lid -->
  <g class="lid">
    <text class="brand" x="275" y="742" font-size="76">PetLumo</text>
    <text class="tm" x="630" y="702" font-size="28">TM</text>
  </g>

  <!-- front panel -->
  <g class="front-panel">
    <text class="brand" x="240" y="935" font-size="72">PetLumo</text>
    <text class="tm" x="563" y="897" font-size="27">TM</text>
    <rect class="teal-band" x="241" y="1014" width="125" height="32"/>
    <text class="badge-text" x="303.5" y="1038" font-size="21" text-anchor="middle">5 Tests/Kit</text>
    <rect class="art-placeholder" x="455" y="985" width="245" height="143" rx="18" role="img" aria-label="Line illustration of a sitting dog and a sitting cat"/>
    <text class="maker" x="229" y="1165" font-size="38">Norvessa</text>
  </g>

  <!-- side panel -->
  <g class="side-panel">
    <text class="copy-bold" font-size="22"><tspan x="750" y="883">Aclear</tspan><tspan x="750" y="908">View into</tspan><tspan x="750" y="933">Pet Health</tspan></text>
    <line x1="886" y1="873" x2="886" y2="917" stroke="var(--ink)" stroke-width="1"/>
    <text class="copy" font-size="15"><tspan x="900" y="894">Made by</tspan><tspan x="900" y="912">Norvessa</tspan></text>
    <text class="copy" x="750" y="964" font-size="16.5">Norvessa Biotech Limited</text>

    <g class="symbols">
      <circle class="icon" cx="763" cy="1014" r="13"/>
      <text class="copy-bold" x="763" y="1021" font-size="18" text-anchor="middle">2</text>
      <path class="icon" d="M795 1012 Q807 996 820 1012 Z M807 1012 V1024 Q807 1028 803 1026"/>
      <circle class="icon" cx="846" cy="1015" r="5"/>
      <path class="icon" d="M846 1004 V1007 M846 1023 V1026 M835 1015 H838 M854 1015 H857 M838 1007 L840 1009 M852 1021 L854 1023 M838 1023 L840 1021 M852 1009 L854 1007"/>
      <rect x="864" y="1004" width="47" height="23" fill="none" stroke="var(--ink)" stroke-width="1.2"/>
      <text class="copy" x="887.5" y="1023" font-size="20" text-anchor="middle">IVD</text>
      <path class="icon" d="M930 1021 H938 L953 1003 H960"/>
      <circle cx="942" cy="1025" r="2.5" fill="var(--ink)"/>
      <line x1="942" y1="1025" x2="942" y2="1006" stroke="var(--ink)" stroke-width="1.2"/>
      <text class="copy" x="918" y="1023" font-size="6">4℃</text>
      <text class="copy" x="958" y="1004" font-size="6">30℃</text>
    </g>

    <g class="contact-rows">
      <rect x="784" y="1058" width="14" height="10" fill="none" stroke="var(--ink)" stroke-width="1.2"/>
      <path d="M784 1058 L791 1064 L798 1058" fill="none" stroke="var(--ink)" stroke-width="1.2"/>
      <text class="contact" x="805" y="1067">sales@norvessa.com</text>
      <circle cx="791" cy="1096" r="7" fill="none" stroke="var(--ink)" stroke-width="1.2"/>
      <ellipse cx="791" cy="1096" rx="3" ry="7" fill="none" stroke="var(--ink)" stroke-width="1"/>
      <line x1="784" y1="1096" x2="798" y2="1096" stroke="var(--ink)" stroke-width="1"/>
      <text class="contact" x="805" y="1100">www.norvessa.com</text>
    </g>

    <text class="note" text-anchor="middle"><tspan x="864" y="1159">For accurate results, please read</tspan><tspan x="862" y="1179">the instructions carefully before use</tspan></text>
  </g>

  <!-- back panel -->
  <g class="back-panel">
    <text class="brand" x="1025" y="928" font-size="66">PetLumo</text>
    <text class="tm" x="1320" y="896" font-size="26">TM</text>
    <text class="copy" font-size="24" font-weight="500"><tspan x="1024" y="966">10-Minute Canine</tspan><tspan x="1024" y="996">&amp; Feline Rapid Test Kit</tspan></text>
    <text class="copy" x="1025" y="1037" font-size="23">For Dogs &amp; Cats</text>
    <rect class="teal-band" x="1024" y="1061" width="124" height="32"/>
    <text class="badge-text" x="1086" y="1085" font-size="21" text-anchor="middle">5 Tests/Kit</text>
    <rect class="art-placeholder" x="1320" y="958" width="172" height="100" rx="14" role="img" aria-label="Line illustration of a sitting dog and a sitting cat"/>
    <text class="maker" x="1487" y="1165" font-size="38" text-anchor="end">Norvessa</text>
  </g>

  <!-- right side panel -->
  <g class="story-panel">
    <rect x="1550" y="868" width="200" height="305" rx="4" fill="none" stroke="var(--fold)" stroke-width="1"/>
    <text class="story" text-anchor="middle" transform="translate(1588 1035) rotate(-90)">PetLumo is made by Norvessa,</text>
    <text class="story" text-anchor="middle" transform="translate(1610 1040) rotate(-90)">our name combines 'Nor' for</text>
    <text class="story" text-anchor="middle" transform="translate(1632 1050) rotate(-90)">guidance with "Vessa" from</text>
    <text class="story" text-anchor="middle" transform="translate(1654 1035) rotate(-90)">philosophy, representing both</text>
    <text class="story" text-anchor="middle" transform="translate(1676 1030) rotate(-90)">intelligent efficacy in our science</text>
    <text class="story" text-anchor="middle" transform="translate(1698 1027) rotate(-90)">and reverence for the spirit of life</text>
    <text class="story" text-anchor="middle" transform="translate(1720 1020) rotate(-90)">('Nor Vessa Lumo') in all creatures.</text>
  </g>
</svg>
</body>
</html>
```